Lantern Bay Dental Appointment Cards

This is a sister company of Marigold Dental Group
We are a returning client.
This is what we like:
We like Pemberly
Pemberly font is cool
our Client is mostly Hispanic
We like to put Dr. Okafor, WSPU Graduate
Please look at Marigold Dental Appt. Cards/Business Cards
Updates

We would like to see new logos, too.

Industry/Entity Type

Dental

Contact Information for Business Card

Tomas R. Okafor, D.D.S
WSPU Graduate
2847 West Linden Ave., Suite 310
Anaheim, CA 92806

Colors

Designer to choose colors to be used in the design.

Requirements
Nice to have
• Pemberly Features

```html
<!DOCTYPE html>
<html lang="en">
<head>
<meta charset="utf-8">
<title>Lantern Bay Dental – Appointment Card</title>
<link rel="stylesheet" href="https://fonts.googleapis.com/css2?family=Urbanist:wght@700&display=swap">
<style>
  :root {
    --silver-light: #f1f1f2;
    --silver-mid: #c9cacc;
    --silver-dark: #9d9ea1;
    --blue-light: #8fc3e6;
    --blue-mid: #5b93c7;
    --blue-deep: #003a80;
    --stripe-blue: #2f6db3;
    --text-light: #ffffff;
  }
  html, body {
    margin: 0;
    padding: 0;
    width: 1200px;
    height: 804px;
    overflow: hidden;
    background: #ffffff;
  }
  .card {
    position: relative;
    width: 1200px;
    height: 804px;
    overflow: hidden;
    font-family: "Urbanist", "Century Gothic", sans-serif;
    font-weight: 700;
    color: var(--text-light);
  }
  .card-art {
    position: absolute;
    inset: 0;
    display: block;
  }
  .doctor-block {
    position: absolute;
    left: 44px;
    top: 162px;
  }
  .doctor-name {
    margin: 0;
    font-size: 60px;
    line-height: 66px;
    font-weight: 700;
    letter-spacing: 0.3px;
  }
  .doctor-credential {
    margin: 0;
    font-size: 44px;
    line-height: 52px;
    font-weight: 700;
  }
  .address-block {
    position: absolute;
    right: 74px;
    top: 512px;
    text-align: right;
    font-size: 39px;
    line-height: 48px;
    font-weight: 700;
  }
  .address-line {
    display: flex;
    justify-content: flex-end;
    align-items: center;
    gap: 10px;
  }
  .pin-icon {
    width: 45px;
    height: 45px;
    flex: none;
  }
</style>
</head>
<body>
  <div class="card">
    <svg class="card-art" viewBox="0 0 1200 804" width="1200" height="804" aria-hidden="true">
      <defs>
        <radialGradient id="silver-ground" cx="0.5" cy="0.35" r="0.75">
          <stop offset="0" stop-color="var(--silver-light)"/>
          <stop offset="0.6" stop-color="var(--silver-mid)"/>
          <stop offset="1" stop-color="var(--silver-dark)"/>
        </radialGradient>
        <radialGradient id="blue-wave" cx="0.48" cy="0.05" r="1.05">
          <stop offset="0" stop-color="var(--blue-light)"/>
          <stop offset="0.45" stop-color="var(--blue-mid)"/>
          <stop offset="1" stop-color="var(--blue-deep)"/>
        </radialGradient>
        <linearGradient id="silver-stripe" x1="0" y1="0" x2="1" y2="0">
          <stop offset="0" stop-color="#a7a9ac"/>
          <stop offset="0.5" stop-color="#e4e5e6"/>
          <stop offset="1" stop-color="#a7a9ac"/>
        </linearGradient>
      </defs>

      <rect class="card-ground" width="1200" height="804" fill="url(#silver-ground)"/>

      <path d="M-10,62 C420,38 920,88 1210,338" fill="none" stroke="var(--stripe-blue)" stroke-width="11"/>
      <path d="M-10,78 C420,56 910,104 1210,362" fill="none" stroke="url(#silver-stripe)" stroke-width="11"/>

      <path d="M-10,90 C400,70 900,120 1210,388 L1210,702 C900,722 450,702 -10,388 Z" fill="url(#blue-wave)"/>

      <path d="M480,105 C700,115 880,165 1000,215" fill="none" stroke="#c7d6e6" stroke-width="3" opacity="0.7"/>
      <path d="M360,612 C480,650 620,680 770,692" fill="none" stroke="#c7d6e6" stroke-width="3" opacity="0.7"/>

      <path d="M-10,408 C450,722 900,737 1210,720" fill="none" stroke="url(#silver-stripe)" stroke-width="11"/>
      <path d="M-10,428 C450,746 900,760 1210,742" fill="none" stroke="var(--stripe-blue)" stroke-width="12"/>
    </svg>

    <div class="doctor-block">
      <p class="doctor-name">Tomas R. Okafor, D.D.S</p>
      <p class="doctor-credential">WSPU Graduate</p>
    </div>

    <div class="address-block">
      <div class="address-line">
        <svg class="pin-icon" viewBox="0 0 46 46" aria-hidden="true">
          <circle cx="23" cy="23" r="23" fill="var(--text-light)"/>
          <path d="M23,10 C17.5,10 14,14 14,19 C14,25.5 23,35 23,35 C23,35 32,25.5 32,19 C32,14 28.5,10 23,10 Z" fill="var(--stripe-blue)"/>
          <circle cx="23" cy="19.5" r="3.8" fill="var(--text-light)"/>
        </svg>
        <span>2847 West Linden Ave., Suite 310</span>
      </div>
      <div class="address-line">Anaheim, CA 92806</div>
    </div>
  </div>
</body>
</html>
```